No Trespassing Jobsite Sign for Construction Company

This Poster is for a 24"X18" 'NO TRESPASSING' job site sign for a construction company.

- please include ALL verbiage as indicated in the 'MOCKUP' attachment
- please include two (2) design options; one with each of the uploaded logos
- we would like to follow the same design as our 'Job Site Safety' which I have also uploaded
- this poster must look professional and sleek

if you have any questions, please send me a message

```html
<!DOCTYPE html>
<html lang="en">
<head>
<meta charset="UTF-8">
<title>No Trespassing Jobsite Sign</title>
<link rel="stylesheet" href="https://fonts.googleapis.com/css2?family=Poppins:wght@400;700;800&family=Source+Serif+4:opsz,wght@8..60,700&display=swap">
<style>
  :root {
    --brand-blue: #2b3288;
    --ink: #2e2e33;
    --white: #ffffff;
    --page: #eceef0;
    --fence-grey: #d6d8dc;
    --tape-yellow: #f6b41c;
    --tape-dark: #1c1c1c;
  }
  * { box-sizing: border-box; margin: 0; padding: 0; }
  html, body { width: 900px; height: 1200px; overflow: hidden; }
  body { background: var(--page); position: relative; }

  .sign {
    position: absolute; left: 20px; top: 278px;
    width: 860px; height: 645px;
    overflow: hidden;
    background: var(--white);
    box-shadow: 0 6px 18px rgba(0,0,0,.25);
  }
  .fence-texture {
    position: absolute; inset: 0;
    background: linear-gradient(90deg, var(--fence-grey) 0%, #f4f5f6 22%, var(--white) 55%);
  }
  .sign-shapes { position: absolute; inset: 0; }

  .headline {
    position: absolute; left: 0; width: 540px; text-align: center;
    font-family: "Poppins", sans-serif; font-weight: 800; color: var(--brand-blue);
    line-height: 1;
  }
  .headline-no { top: 8px; font-size: 150px; letter-spacing: -4px; left: 12px; }
  .headline-trespassing { top: 143px; font-size: 72px; letter-spacing: -1px; left: -10px; }

  .warning-copy {
    position: absolute; left: 30px; width: 520px; top: 229px;
    font-family: "Poppins", sans-serif; font-weight: 400; font-size: 19.5px;
    line-height: 33px; color: var(--ink); text-align: center;
  }
  .slogan {
    position: absolute; left: 40px; width: 440px; top: 325px;
    font-family: "Source Serif 4", serif; font-weight: 700; font-size: 46px;
    line-height: 58px; color: var(--brand-blue); text-align: center; letter-spacing: -1px;
  }
  .web-address {
    position: absolute; left: 24px; top: 470px;
    font-family: "Poppins", sans-serif; font-weight: 700; font-size: 28px;
    letter-spacing: 2px; color: var(--white); line-height: 44px;
  }
  .license {
    position: absolute; left: 242px; top: 521px;
    font-family: "Poppins", sans-serif; font-weight: 800; font-size: 19px;
    letter-spacing: 2px; color: var(--brand-blue);
  }

  .company-block {
    position: absolute; left: 560px; width: 290px; top: 206px;
    color: var(--white); font-family: "Source Serif 4", serif; font-weight: 700;
    text-align: center;
  }
  .company-role { font-size: 40px; line-height: 38px; }
  .company-rule { height: 1.5px; background: var(--white); margin: 15px 6px 18px; }
  .company-name { font-size: 58px; line-height: 58px; }
  .company-suffix { font-size: 34px; line-height: 40px; }
</style>
</head>
<body>
  <main class="sign" aria-label="No trespassing jobsite sign">
    <div class="fence-texture" role="img" aria-label="Faint chain-link fence backdrop"></div>

    <svg class="sign-shapes" width="860" height="645" viewBox="0 0 860 645" aria-hidden="true">
      <polygon points="701,0 860,0 860,645 332,645" fill="var(--brand-blue)"/>
      <polygon points="860,434 860,645 755,645" fill="var(--white)"/>
      <polygon points="0,469 500,469 474,513 0,513" fill="var(--brand-blue)"/>
    </svg>

    <h1 class="headline headline-no">NO</h1>
    <h2 class="headline headline-trespassing">TRESPASSING</h2>

    <p class="warning-copy">This is a Designated Construction Site.<br>Anyone Tresspassing on this Property, upon<br>conviction, shall be Guilty of a Felony.</p>

    <p class="slogan">“We Build Lasting<br>Trust”®</p>

    <p class="web-address">www.harlowbuilds.net</p>
    <p class="license">CGC7741902</p>

    <div class="company-block">
      <p class="company-role">General<br>Contractors</p>
      <div class="company-rule"></div>
      <p class="company-name">Harlow &amp;</p>
      <p class="company-suffix">Sons, Inc.</p>
    </div>

    <svg class="sign-shapes" width="860" height="645" viewBox="0 0 860 645" role="img" aria-label="Crossed caution tape strips along the bottom edge">
      <polygon points="0,546 860,590 860,618 0,574" fill="var(--tape-yellow)"/>
      <polygon points="380,645 860,548 860,572 500,645" fill="var(--tape-yellow)"/>
      <polygon points="0,634 860,458 860,474 0,650" fill="var(--tape-yellow)"/>
      <line x1="0" y1="546" x2="860" y2="590" stroke="var(--tape-dark)" stroke-width="2"/>
      <line x1="0" y1="574" x2="860" y2="618" stroke="var(--tape-dark)" stroke-width="2"/>
    </svg>
  </main>
</body>
</html>
```